Child care/Preparatory Business Card Design & logo design

I need a logo to use on a business card, letterhead, uniform and promotional material for a new business called 'Kestrel Ridge Preparatory'. It is located in the north west of Western Australia in the Pilbara region. The service will provide a 'Preparation for Education' program for 3 and 4 year old children. I would like a logo that shows unity, or belonging in children. I like the colour blue, any primary colours would be suitable. The design needs to be cheerful and appealing to children whilst still having an 'elite' edge to it.

Target Market(s)

Families with young children

Industry/Entity Type

Business

Contact Information for Business Card

Marcia Hollis Director
Kestrel Ridge Preparatory
M 0491 570 318
office@kestrelridgeprep.com.au
PO Box 581 Tarrent WA 6731

Preparation for Education

```html
<!DOCTYPE html>
<html lang="en">
<head>
<meta charset="utf-8">
<title>Kestrel Ridge Preparatory – Business Card</title>
<link rel="stylesheet" href="https://fonts.googleapis.com/css2?family=Poppins:wght@600&family=Questrial&display=swap">
<style>
  :root {
    --sky: #45cdfb;
    --paper: #ffffff;
    --backdrop: #e8e5e1;
    --ink-on-sky: #ffffff;
    --card-shadow: rgba(0, 0, 0, 0.18);
  }
  * { box-sizing: border-box; margin: 0; padding: 0; }
  html, body {
    width: 1200px; height: 1000px; overflow: hidden;
    background: var(--backdrop);
  }
  .canvas {
    position: relative; width: 1200px; height: 1000px;
  }
  .card {
    position: absolute; left: 220px; width: 760px; height: 434px;
    background: var(--paper); border-radius: 34px; overflow: hidden;
    box-shadow: 0 6px 22px var(--card-shadow);
  }
  .card--front { top: 46px; }
  .card--back { top: 520px; }

  /* Front */
  .brand {
    position: absolute; left: 0; right: 0; top: 0; bottom: 0;
    display: flex; align-items: center; justify-content: center; gap: 22px;
  }
  .brand__dot {
    width: 74px; height: 74px; border-radius: 50%; background: var(--sky); flex: none;
  }
  .brand__name {
    font-family: "Poppins", sans-serif; font-weight: 600;
    font-size: 44px; color: var(--sky); letter-spacing: 0.5px; white-space: nowrap;
  }

  /* Back */
  .back__mark {
    position: absolute; left: 50%; top: 44px; width: 120px; height: 120px;
    margin-left: -60px; border-radius: 50%; background: var(--sky);
  }
  .holder {
    position: absolute; left: 0; right: 0; top: 178px; text-align: center;
    color: var(--sky);
  }
  .holder__name {
    font-family: "Poppins", sans-serif; font-weight: 600; font-size: 34px; line-height: 1.15;
  }
  .holder__role {
    font-family: "Questrial", sans-serif; font-size: 29px; line-height: 1.2;
  }
  .contact-band {
    position: absolute; left: 0; right: 0; bottom: 0; height: 156px;
    background: var(--sky); color: var(--ink-on-sky);
    font-family: "Questrial", sans-serif;
  }
  .address {
    position: absolute; left: 44px; top: 24px; font-size: 24px; line-height: 1.3;
  }
  .reach {
    position: absolute; right: 36px; bottom: 18px; font-size: 24px; line-height: 1.45;
    text-align: right;
  }
  .reach__line { display: flex; align-items: center; justify-content: flex-end; gap: 10px; }
  .reach__icon { width: 20px; height: 20px; flex: none; }
</style>
</head>
<body>
<main class="canvas">

  <section class="card card--front" aria-label="Card front">
    <div class="brand">
      <span class="brand__dot" aria-hidden="true"></span>
      <span class="brand__name">Kestrel Ridge Preparatory</span>
    </div>
  </section>

  <section class="card card--back" aria-label="Card back">
    <span class="back__mark" aria-hidden="true"></span>
    <div class="holder">
      <p class="holder__name">Marcia Hollis</p>
      <p class="holder__role">Director Kestrel Ridge Preparatory</p>
    </div>
    <div class="contact-band">
      <p class="address">PO Box<br>581 Tarrent WA 6731<br>Preparation for Education</p>
      <div class="reach">
        <p class="reach__line">0491 570 318
          <svg class="reach__icon" viewBox="0 0 24 24" aria-hidden="true">
            <path fill="#fff" d="M6.6 10.8a15.1 15.1 0 0 0 6.6 6.6l2.2-2.2a1 1 0 0 1 1-.25 11.4 11.4 0 0 0 3.6.57 1 1 0 0 1 1 1V20a1 1 0 0 1-1 1A17 17 0 0 1 3 4a1 1 0 0 1 1-1h3.5a1 1 0 0 1 1 1c0 1.25.2 2.45.57 3.57a1 1 0 0 1-.25 1z"/>
          </svg>
        </p>
        <p class="reach__line">office@kestrelridgeprep.com.au
          <svg class="reach__icon" viewBox="0 0 24 24" aria-hidden="true">
            <rect x="2.5" y="5.5" width="19" height="13" fill="none" stroke="#fff" stroke-width="1.8"/>
            <path d="M2.5 5.5l9.5 7.5 9.5-7.5M2.5 18.5l7-6M21.5 18.5l-7-6" fill="none" stroke="#fff" stroke-width="1.6"/>
          </svg>
        </p>
      </div>
    </div>
  </section>

</main>
</body>
</html>
```